plumbing & gas fitting business card design

We need a business card design for a plumbing & gas fitting company. The company covers commercial, domestic and maintenance work. We would like a modern design communicating efficiency and sophistication. preferred colours would include (red grey & black) or (green grey & black). Please DO NOT include any water droplets.

Varcoe Plumbing & Gas, Commercial Domestic & Maintenance, licence no. 418736K, ABN 57204918362, Phone 0417382965, Email varcoeplumbingandgas@tidemail.com

```html
<!DOCTYPE html>
<html lang="en">
<head>
<meta charset="utf-8">
<title>Varcoe Plumbing &amp; Gas – Business Card</title>
<link href="https://fonts.googleapis.com/css2?family=Open+Sans:wght@400;600;700&display=swap" rel="stylesheet">
<style>
  :root {
    --page-bg: #e4e5e7;
    --card-black: #1b1b1b;
    --card-black-light: #2b2b2b;
    --brand-green: #5aa544;
    --brand-green-dark: #3e8a33;
    --pipe-green-light: #9fd67f;
    --pipe-green: #4d9f30;
    --text-white: #ffffff;
  }
  html, body {
    margin: 0;
    padding: 0;
    width: 1200px;
    height: 1048px;
    overflow: hidden;
    background: var(--page-bg);
    font-family: "Open Sans", Arial, sans-serif;
  }
  .sheet {
    position: relative;
    width: 1200px;
    height: 1048px;
  }
  .card {
    position: absolute;
    left: 210px;
    width: 780px;
    height: 477px;
    overflow: hidden;
    box-shadow: 0 6px 18px rgba(0,0,0,0.25);
  }
  .card-front {
    top: 32px;
    background:
      repeating-linear-gradient(90deg, rgba(255,255,255,0.025) 0 2px, rgba(0,0,0,0.04) 2px 5px),
      linear-gradient(160deg, var(--card-black-light), var(--card-black));
  }
  .card-back {
    top: 539px;
    background: linear-gradient(160deg, var(--brand-green), var(--brand-green-dark));
  }
  .pipe-art {
    position: absolute;
    inset: 0;
  }
  .wordmark {
    color: var(--text-white);
    font-weight: 600;
    line-height: 1;
  }
  .wordmark-name {
    display: block;
    text-transform: uppercase;
    letter-spacing: 2px;
  }
  .wordmark-trade {
    display: block;
    letter-spacing: 4px;
  }
  .card-front .wordmark {
    position: absolute;
    left: 240px;
    top: 212px;
  }
  .card-front .wordmark-name { font-size: 62px; }
  .card-front .wordmark-trade { font-size: 28px; margin-top: 6px; }

  .card-back .wordmark {
    position: absolute;
    left: 44px;
    top: 172px;
  }
  .card-back .wordmark-name { font-size: 44px; }
  .card-back .wordmark-trade { font-size: 20px; margin-top: 5px; letter-spacing: 3px; }

  .divider {
    position: absolute;
    left: 296px;
    top: 120px;
    width: 3px;
    height: 262px;
    background: var(--text-white);
  }
  .contact {
    position: absolute;
    left: 312px;
    top: 150px;
    margin: 0;
    padding: 0;
    list-style: none;
    color: var(--text-white);
    font-size: 17px;
    line-height: 27px;
  }
  .contact .services { font-weight: 700; }
  .contact strong { font-weight: 700; }
</style>
</head>
<body>
<main class="sheet">

  <section class="card card-front" aria-label="Business card front">
    <svg class="pipe-art" width="780" height="477" viewBox="0 0 780 477" role="img" aria-label="Green pipe illustration running from the top right and bottom left toward the name">
      <defs>
        <linearGradient id="pipeTone" x1="0" y1="0" x2="0" y2="1">
          <stop offset="0" stop-color="var(--pipe-green-light)"/>
          <stop offset="1" stop-color="var(--pipe-green)"/>
        </linearGradient>
      </defs>
      <rect x="400" y="18" width="360" height="160" rx="24" fill="url(#pipeTone)" opacity="0.3"/>
      <rect x="40" y="345" width="380" height="115" rx="24" fill="url(#pipeTone)" opacity="0.3"/>
    </svg>
    <div class="wordmark">
      <span class="wordmark-name">Varcoe</span>
      <span class="wordmark-trade">plumbing &amp; gas</span>
    </div>
  </section>

  <section class="card card-back" aria-label="Business card back">
    <div class="wordmark">
      <span class="wordmark-name">Varcoe</span>
      <span class="wordmark-trade">plumbing &amp; gas</span>
    </div>
    <div class="divider"></div>
    <ul class="contact">
      <li class="services">Commercial Domestic &amp; Maintenance</li>
      <li>licence no <strong>418736K</strong></li>
      <li>ABN <strong>57204918362</strong></li>
      <li>Phone <strong>0417382965</strong></li>
      <li>Email <strong>varcoeplumbingandgas@tidemail.com</strong></li>
    </ul>
  </section>

</main>
</body>
</html>
```